Home page design for car dealership (Brisk Roadhouse - 1585)

The client wants to update his current website: http://www.briskroadhouse-example.com/
You can find the dealer info on their current site.

Please use the instructions provided by the dealer to provide new design mockups:

montarocars-example.com- use the main background

garyholtbuick-example.com - wants a large slideshow with 4 large buttons below it: Inventory, Contact Us, Vendo Wheels and Pinwall. Use 2 of their showroom pictures for the button images. For Vendo and Pinwall, keep the company's logo

Have fun and let me know if there's any questions!
Updates

Hello everyone! I've sent the mockups provided to the client and as soon as I get feedback, I will notify you individually of their decision, or revisions, if needed. Thanks so much for your patience! Mirabel

Industry/Entity Type

Dealership

```html
<!DOCTYPE html>
<html lang="en">
<head>
<meta charset="utf-8">
<title>Brisk Roadhouse – Home</title>
<link href="https://fonts.googleapis.com/css2?family=Play:wght@400;700&family=Lato:wght@400;700&family=Open+Sans:wght@400;600&display=swap" rel="stylesheet">
<style>
:root{
  --red:#7a0808;
  --red-deep:#5c0505;
  --red-bright:#b01010;
  --ink:#2b2b2b;
  --muted:#666;
  --line:#dcdcdc;
  --footer:#f3f3f3;
  --accent-blue:#1aa3e6;
  --white:#fff;
}
*{box-sizing:border-box;margin:0;padding:0}
html,body{width:1083px;height:1200px;overflow:hidden;background:var(--white);font-family:"Lato",sans-serif;color:var(--ink)}
.page{position:relative;width:1083px;height:1200px}
.abs{position:absolute}

/* header */
.nav-band{left:0;top:52px;width:1083px;height:31px;background:linear-gradient(#8a0a0a,var(--red-deep))}
.brand{left:125px;top:0;width:294px;height:83px;background:linear-gradient(120deg,var(--red-bright),var(--red-deep));display:flex;align-items:center;justify-content:center;gap:10px}
.brand-mark{width:14px;height:14px;border-radius:50%;background:var(--white)}
.brand-name{font-family:"Play",sans-serif;font-weight:700;font-size:27px;color:var(--white);letter-spacing:.5px}
.top-address{left:558px;top:21px;font-family:"Open Sans",sans-serif;font-size:10.5px;color:#333}
.top-phone{left:792px;top:12px;display:flex;align-items:center;gap:6px;font-family:"Play",sans-serif;font-size:20px;color:var(--red)}
.main-nav{right:125px;top:52px;height:31px;display:flex;gap:0}
.main-nav a{display:block;color:var(--white);text-decoration:none;font-size:12px;line-height:31px;padding:0 17px;position:relative;font-family:"Lato",sans-serif}
.main-nav a:last-child{padding-right:0}
.main-nav a.active::after{content:"";position:absolute;left:50%;bottom:-5px;margin-left:-5px;border:5px solid transparent;border-top-color:var(--red-deep);border-bottom:0}

/* hero */
.hero{left:0;top:83px;width:1083px;height:307px;background:linear-gradient(100deg,#0c0c0c 0%,#1c1c1c 30%,#3a3d42 55%,#232427 80%,#0d0d0d 100%)}
.hero-stripe{left:0;top:83px;width:1083px;height:307px}
.hero-photo{left:410px;top:95px;width:520px;height:260px;border-radius:40px;background:radial-gradient(ellipse at 55% 55%,#1a1a1a 0%,#2d2f33 55%,rgba(60,62,66,0) 75%)}
.hero-title{left:140px;top:186px;font-family:"Lato",sans-serif;font-size:22px;line-height:26px;color:var(--white)}
.hero-link{left:142px;top:303px;font-size:11px;font-weight:700;color:var(--accent-blue);letter-spacing:-.2px}

/* tiles */
.tile{top:417px;width:198px;height:83px;background:linear-gradient(#fafafa,#e9e9e9);box-shadow:0 1px 3px rgba(0,0,0,.25);overflow:hidden}
.tile-title{position:absolute;font-family:"Play",sans-serif;font-size:18px;color:var(--red-deep)}
.tile-more{position:absolute;left:16px;bottom:10px;font-size:9.5px;color:#888;display:flex;align-items:center;gap:5px}
.tile-more i{display:block;width:12px;height:7px;border-top:1px solid #999;border-bottom:1px solid #999;position:relative}
.tile-more i::after{content:"";position:absolute;left:0;right:0;top:2px;border-top:1px solid #999}
.tile-art{position:absolute}

/* welcome */
.welcome-title{left:129px;top:539px;font-family:"Play",sans-serif;font-size:20px;font-weight:700;color:#333}
.welcome-copy{left:129px;top:577px;width:590px;font-size:11.6px;line-height:16.7px;color:#222}
.welcome-copy p+p{margin-top:16.7px}
.showroom{left:743px;width:215px;height:74px;background:linear-gradient(110deg,#c9a43c,#6e5a3b 40%,#3b2d2a 70%,#b8b3a8)}
.divider{left:90px;top:733px;width:903px;height:1px;background:linear-gradient(90deg,transparent,#ddd 15%,#ddd 85%,transparent)}

/* featured */
.featured-title{left:0;width:1083px;top:746px;text-align:center;font-family:"Open Sans",sans-serif;font-size:21px;color:#333}
.thumb{top:792px;width:130px;height:74px;border:1px solid var(--line);background:var(--white);display:flex;align-items:center;justify-content:center}
.thumb span{display:block;width:96px;height:38px;border-radius:18px 22px 8px 8px}
.arrow{top:816px}

/* footer */
.footer{left:0;top:914px;width:1083px;height:238px;background:var(--footer);border-top:1px solid #d5d5d5}
.footer-rule{left:0;top:952px;width:1083px;height:1px;background:#d5d5d5}
.foot-head{top:927px;font-family:"Open Sans",sans-serif;font-size:12.5px;color:#444}
.foot-list{top:962px;list-style:none;font-family:"Open Sans",sans-serif;font-size:9.5px;line-height:19.2px;color:#333}
.foot-loc{left:413px;top:959px;font-family:"Open Sans",sans-serif;font-size:9.2px;line-height:15px;color:#333}
.foot-loc b{font-weight:600;font-size:10px}
.foot-loc .gap{height:11px}
.social{left:618px;height:25px;border-radius:13px;display:flex;align-items:center;gap:6px;padding:0 10px 0 8px;color:var(--white);font-family:"Open Sans",sans-serif;font-weight:600;font-size:10px;box-shadow:0 1px 2px rgba(0,0,0,.3)}
.social i{width:12px;height:12px;border-radius:50%;background:var(--white);display:block}
.social.fan{top:966px;background:linear-gradient(#9a1a1a,var(--red-deep))}
.social.chirp{top:1002px;background:linear-gradient(#5bc3f0,#1a98d8)}
.social.rss{top:1041px;background:linear-gradient(#ffc04a,#f08a14)}
.news{left:797px;font-family:"Open Sans",sans-serif;font-size:9.8px;color:#333}
.field{left:797px;width:153px;height:22px;background:var(--white);border:1px solid #bbb}
.check{left:797px;top:1069px;width:10px;height:10px;border:1px solid #bbb;background:var(--white)}
.submit{left:795px;top:1091px;width:78px;height:22px;background:linear-gradient(#555,#333);color:var(--white);font-family:"Open Sans",sans-serif;font-weight:700;font-size:10px;display:flex;align-items:center;justify-content:center;border-radius:2px}
.bottom{left:0;top:1152px;width:1083px;height:48px;background:linear-gradient(#e8e8e8,#fafafa);border-top:1px solid #d5d5d5}
.bottom-left{left:127px;top:1169px;font-size:9.5px;color:#333}
.bottom-right{right:128px;top:1169px;font-size:9.5px;color:#333}
</style>
</head>
<body>
<div class="page">

  <!-- Header -->
  <div class="abs nav-band"></div>
  <div class="abs brand"><span class="brand-mark"></span><span class="brand-name">Brisk Roadhouse</span></div>
  <div class="abs top-address">4820 Calder Ridge Rd Austin , Texas 78700</div>
  <div class="abs top-phone">
    <svg width="20" height="16" viewBox="0 0 20 16" aria-hidden="true"><path d="M2 5c0-3 16-3 16 0v2h-4V5H6v2H2z" fill="#7a0808"/><rect x="4" y="8" width="12" height="7" rx="1.5" fill="#7a0808"/><circle cx="10" cy="11.5" r="2" fill="#fff"/></svg>
    <span>512-555-0184</span>
  </div>
  <nav class="abs main-nav">
    <a class="active">HOME</a><a>INVENTORY</a><a>VEHICLE FINDER</a><a>FINANCING</a><a>CONTACT US</a>
  </nav>

  <!-- Hero -->
  <div class="abs hero"></div>
  <svg class="abs hero-stripe" width="1083" height="307" viewBox="0 0 1083 307" aria-hidden="true">
    <polygon points="60,0 140,0 330,307 250,307" fill="#ffffff" opacity=".04"/>
    <polygon points="980,0 1083,0 1083,120 1040,307 1000,307" fill="#8a0a0a" opacity=".35"/>
  </svg>
  <div class="abs hero-photo" role="img" aria-label="Black compact hatchback parked in a garage"></div>
  <div class="abs hero-title">Contrary to popular belief<br>There are many variations</div>
  <div class="abs hero-link">with Rear View Cameral ›</div>

  <!-- Tiles -->
  <div class="abs tile" style="left:125px">
    <div class="tile-title" style="left:45px;top:5px">INVENTORY</div>
    <div class="tile-art" role="img" aria-label="Row of assorted cars" style="left:0;top:33px;width:198px;height:30px;background:linear-gradient(90deg,#b61818,#2a3f8a 25%,#e8e8e8 45%,#6a1010 65%,#5a5a5a 85%,#8a8a8a)"></div>
    <div class="tile-more"><i></i>More</div>
  </div>
  <div class="abs tile" style="left:337px">
    <div class="tile-art" role="img" aria-label="Close-up of a yellow car rear" style="left:90px;top:0;width:108px;height:83px;background:linear-gradient(100deg,rgba(233,233,233,0),#d9a21a 35%,#8a8a8a 75%,#cfcfcf)"></div>
    <div class="tile-title" style="left:17px;top:8px">Contact Us</div>
    <div class="tile-more"><i></i>More</div>
  </div>
  <div class="abs tile" style="left:548px">
    <div class="tile-title" style="left:26px;top:24px;font-size:20px;font-weight:700;color:#333">Vendo Wheels</div>
    <div class="tile-more"><i></i>More</div>
  </div>
  <div class="abs tile" style="left:760px">
    <div class="tile-title" style="left:48px;top:22px;font-size:22px;font-weight:700;color:#333"><span style="display:inline-block;width:10px;height:10px;background:var(--red);margin-right:8px;vertical-align:middle"></span>Pinwall</div>
    <div class="tile-more"><i></i>More</div>
  </div>

  <!-- Welcome -->
  <h1 class="abs welcome-title">Welcome to Brisk Roadhouse</h1>
  <div class="abs welcome-copy">
    <p>Brisk Roadhouse has been the premier dealership in the super car culture of Austin Texas for the last 27 years. We specialize in unique and exotic cars exclusively picked by the owner and car enthusiast himself, Dorian Kessler (known and endeared as DK).</p>
    <p>DK takes great pride in the quality of his inventory. As a second generation luxury car dealership owner, his knowledge and experience is unparalleled. Whether you are in the market for an exotic super car, a modified street car, or a reliable family vehicle, we are excited to share our passion with you.</p>
  </div>
  <div class="abs showroom" style="top:541px" role="img" aria-label="Showroom floor with yellow and white sports cars"></div>
  <div class="abs showroom" style="top:623px;background:linear-gradient(110deg,#d8c25a,#3a2020 35%,#9a1515 55%,#2a2a2a 80%,#c9c4b8)" role="img" aria-label="Showroom with red and black exotic cars"></div>
  <div class="abs divider"></div>

  <!-- Featured -->
  <h2 class="abs featured-title" style="font-weight:400">Featured Vehicles</h2>
  <svg class="abs arrow" style="left:133px" width="14" height="26" viewBox="0 0 14 26" aria-hidden="true"><path d="M11 3 3 13l8 10" stroke="#111" stroke-width="3" fill="none"/></svg>
  <svg class="abs arrow" style="left:933px" width="14" height="26" viewBox="0 0 14 26" aria-hidden="true"><path d="M3 3l8 10-8 10" stroke="#111" stroke-width="3" fill="none"/></svg>
  <div class="abs thumb" style="left:163px"><span role="img" aria-label="Yellow sports coupe" style="background:linear-gradient(#f2cc1a,#c99a08)"></span></div>
  <div class="abs thumb" style="left:319px"><span role="img" aria-label="Silver SUV" style="background:linear-gradient(#e2e2e2,#9a9a9a)"></span></div>
  <div class="abs thumb" style="left:476px"><span role="img" aria-label="Black luxury sedan" style="background:linear-gradient(#4a4a4a,#0e0e0e)"></span></div>
  <div class="abs thumb" style="left:632px"><span role="img" aria-label="Red compact hatchback" style="background:linear-gradient(#e03040,#9a0c18)"></span></div>
  <div class="abs thumb" style="left:788px"><span role="img" aria-label="Silver hybrid hatchback" style="background:linear-gradient(#d8d8d8,#8c8c8c)"></span></div>

  <!-- Footer -->
  <div class="abs footer"></div>
  <div class="abs footer-rule"></div>
  <div class="abs foot-head" style="left:127px">Sitemap</div>
  <div class="abs foot-head" style="left:260px">About</div>
  <div class="abs foot-head" style="left:413px;top:924px">Our Location:</div>
  <div class="abs foot-head" style="left:617px">Connect With Us</div>
  <div class="abs foot-head" style="left:797px">Sign up to our newsletter</div>
  <ul class="abs foot-list" style="left:127px"><li>HOME</li><li>INVENTORY</li><li>VEHICLE FINDER</li><li>FINANCING</li><li>CONTACT US</li></ul>
  <ul class="abs foot-list" style="left:260px"><li>Lorem Ipsum</li><li>About Us</li><li>Lorem Ipsum</li><li>Lorem Ipsum</li><li>Partnerships</li><li>Join Us</li><li>Careers</li></ul>
  <div class="abs foot-loc">
    <b>Brisk Roadhouse</b><br>4820 Calder Ridge Rd<br>Austin , Texas 78700<br>512-555-0184
    <div class="gap"></div>
    <b>Hours of Operation</b><br>Mon-Fri: 9:00AM - 6:00PM<br>Saturday: 10:00AM - 3:00PM<br>Sunday: Closed
  </div>
  <div class="abs social fan"><i></i>Become a Fan</div>
  <div class="abs social chirp"><i></i>Follow on Chirpline</div>
  <div class="abs social rss"><i></i>Subscribe to RSS</div>
  <div class="abs news" style="top:962px">Your Name</div>
  <div class="abs field" style="top:982px"></div>
  <div class="abs news" style="top:1013px">Your Email Address</div>
  <div class="abs field" style="top:1032px"></div>
  <div class="abs check"></div>
  <div class="abs news" style="left:819px;top:1067px">I agree to recieve newsletter</div>
  <div class="abs submit">Submit</div>

  <div class="abs bottom"></div>
  <div class="abs bottom-left">CAR DEALER WEBSITES BY DEALERFORGE</div>
  <div class="abs bottom-right">COPYRIGHT © 2003-2014 DEALERFORGE, LTD. ALL RIGHTS RESERVED.</div>
</div>
</body>
</html>
```